依頼詳細
置き配指示表示プレート「ポナレト」の先行販売チラシです。
今月から現在ツバネコにて先行販売してますが、デザイン力不足もあり販売不調です。
ツバネコ画像にも使います。パッケージデザインにも使う予定です。

デザインは全くのおまかせです。

B5チラシも添付しましたが、商品説明なので、こちらも参考にしてもらえればいいかと思います。
記載項目
ポナレト(なるべく大きく表記してほしいです。商標登録も申請済)
商品写真(いいのが無いのですが、あたりだけ付けてくれてもOKです)
インターホン付近に設置
置き配
非対面(非接触もOK)

サイズ:約W150×H75 厚み13mm
プレート素材:ポリスチレン・コルク
シール素材:塩ビ・ラミネート
カード素材:紙
ラミネート素材:PET
サイズ
A4
ページ数
片面
希望イメージ
シンプル 複雑
単色 カラフル
暗い 明るい
日常 高級
遊び心 厳粛
未来的 伝統的
女性的 男性的
希望する色
納品ファイル
• 高解像度JPG (.jpg)
• イラストレーター形式 (.ai)
補足説明
「ポナレト」のロゴはありません。好きな書体デザインでOKです。
■ 選んだ理由

配達員女性が「了解しました」の一言で商品が分かりやすくなっており大変気に入りました。
荷受人だけでなく、配達員の立場も考慮していただけた事が決め手でした。
その後の修正も早くしていただきありがとうございました。

■ 提案者全員のお礼・コメント

皆さんとても素晴らしいデザイン力で本当にありがとうございました。
今回初めての発注者の立場でしたが、また利用したくなりました。
皆さん、また是非お願いしたい方々ばかりです。

```html
<!DOCTYPE html>
<html lang="ja">
<head>
<meta charset="utf-8">
<title>置き配指示表示プレート ポナレト</title>
<link href="https://fonts.googleapis.com/css2?family=Noto+Sans+JP:wght@500;700;900&display=swap" rel="stylesheet">
<style>
:root{
  --ink:#1b1b1f;
  --navy:#1d2a4a;
  --brand:#1f5fae;
  --yellow:#ffe14a;
  --paper:#f3f3f1;
  --wall-a:#e9e9e6;
  --wall-b:#cfd0cd;
  --cork-a:#a7774b;
  --cork-b:#7d5332;
  --line:#9a9a9a;
}
*{box-sizing:border-box;margin:0;padding:0}
html,body{width:849px;height:1200px;overflow:hidden}
body{font-family:"Noto Sans JP",sans-serif;color:var(--ink);background:var(--paper)}
.flyer{position:relative;width:849px;height:1200px;overflow:hidden;
  background:radial-gradient(ellipse at 40% 30%,var(--wall-a),var(--wall-b))}
.lead{position:absolute;left:40px;top:30px;font-weight:900;font-size:32px;line-height:1.5;letter-spacing:1px}
.badge{position:absolute;right:22px;top:12px;width:170px;height:170px;border-radius:50%;
  background:var(--yellow);border:6px solid var(--navy);display:flex;align-items:center;justify-content:center;
  text-align:center;font-weight:900;font-size:28px;line-height:1.3;color:var(--navy)}
.band{position:absolute;left:60px;top:170px;width:600px;height:66px;background:var(--navy);
  color:#fff;font-weight:900;font-size:34px;display:flex;align-items:center;justify-content:center;letter-spacing:3px}
.brand{position:absolute;left:250px;top:245px;font-weight:900;font-size:118px;color:var(--brand);letter-spacing:10px;line-height:1}
.intercom{position:absolute;left:0;top:250px;width:215px;height:600px;
  background:linear-gradient(180deg,#d9dad8,#b9bab7)}
.plate{position:absolute;left:212px;top:420px;width:610px;height:350px;
  background:linear-gradient(135deg,var(--cork-a),var(--cork-b));box-shadow:0 6px 14px rgba(0,0,0,.25)}
.note{position:absolute;left:40px;top:800px;background:#fff;border:2px solid var(--ink);
  padding:8px 14px;font-weight:700;font-size:17px;line-height:1.4;transform:rotate(-4deg)}
.note b{color:var(--brand)}
.cards{position:absolute;left:110px;top:858px;width:232px;height:104px;background:linear-gradient(90deg,#3a5da8,#f0d23c,#e7e7e7)}
.points{position:absolute;left:425px;top:838px;font-weight:900;font-size:23px;line-height:1.55}
.points .em{color:var(--brand)}
.specs{position:absolute;left:110px;top:975px;border-collapse:collapse;font-size:13px}
.specs th{background:var(--navy);color:#fff;font-weight:700;padding:6px 8px;text-align:left;white-space:nowrap;border:1px solid var(--line)}
.specs td{background:#fff;padding:6px 8px;border:1px solid var(--line);white-space:nowrap}
.boxes{position:absolute;left:640px;top:990px;width:170px;height:110px;background:linear-gradient(180deg,#d7ae78,#b78550)}
.tags{position:absolute;left:560px;top:1115px;display:flex;flex-direction:column;gap:8px;align-items:flex-end;width:270px}
.tag{background:var(--navy);color:#fff;font-weight:700;font-size:18px;padding:4px 14px}
</style>
</head>
<body>
<main class="flyer">
  <p class="lead">面倒なネットでの置き配指示も不要?!<br>インターホン付近に設置するだけ!</p>
  <div class="badge">現役<br>宅配ドライバー<br>考案!</div>
  <div class="band">置き配指示表示プレート</div>
  <h1 class="brand">ポナレト</h1>
  <div class="intercom" role="img" aria-label="玄関のインターホンが付いた外壁の写真"></div>
  <div class="plate" role="img" aria-label="コルク製の置き配指示表示プレートにメッセージカードを差し込んだ商品写真"></div>
  <p class="note">状況に合わせて使える<br><b>各メッセージカード・シール</b>を同封!</p>
  <div class="cards" role="img" aria-label="同封のメッセージカードとシールの見本"></div>
  <p class="points">張り替え可能な、<span class="em">カードorシール</span>で<br>置き配場所や時間指定!<br><span class="em">インターホン付近に設置</span>で確実に<br>宅配員に見てもらえる!</p>
  <table class="specs">
    <tr><th>サイズ</th><td>約W150×H75 厚み13mm</td><th>カード素材</th><td>紙</td></tr>
    <tr><th>プレート素材</th><td>ポリスチレン・コルク</td><th>ラミネート素材</th><td>PET</td></tr>
    <tr><th>シール素材(全12種類)</th><td colspan="3">塩ビ・ラミネート</td></tr>
  </table>
  <div class="boxes" role="img" aria-label="積み重ねた段ボール箱のイラスト"></div>
  <div class="tags">
    <span class="tag">#置き配</span>
    <span class="tag">#非対面(非接触もOK)</span>
  </div>
</main>
</body>
</html>
```